Communication of Recommended Belief Letter

To Whom This May Concern,

My company's name is Bramwell LLC. I would like to send electronic messages to my clients. Therefore, I would like PixelHarbor to create a letterhead template to say Bramwell- without the LLC. My messages could extend up to 20 pages long. I would like something that is chic, fancy, and has creative designs. The background color should be white. The creative designs are open for suggestions without color restrictions. Font type and color are also open for suggestions. It may be what you believe best suite's the letterhead. I would like the letterhead to include the company logo. Please see attachment for file. Thank you.

Target Market(s)

working class American's

Industry/Entity Type

Communication

Contact Information for Business Card

The business card should be chic and fancy.

Font styles to use
Script

Requirements
Must have
• Company name: Bramwell LLC
• Company symbol: Please see attachment
• Name: Marisol Denby
• Title: President
• Company website: www.bramwellllc-example.com
Nice to have
• Open for suggestions

```html
<!DOCTYPE html>
<html lang="en">
<head>
<meta charset="utf-8">
<title>Bramwell Letterhead</title>
<link rel="stylesheet" href="https://fonts.googleapis.com/css2?family=Cinzel:wght@400&family=Noto+Serif:ital,wght@0,700;1,400&family=Open+Sans:wght@400&display=swap">
<style>
  :root {
    --backdrop: #c2cece;
    --paper: #ffffff;
    --ink-dark: #1a1f1f;
    --accent-yellow: #ecc90a;
    --brand-gold: #a87414;
    --text-light: #ffffff;
  }
  html, body {
    margin: 0;
    padding: 0;
    width: 1200px;
    height: 1200px;
    overflow: hidden;
    background: var(--backdrop);
  }
  .letterhead {
    position: absolute;
    left: 216px;
    top: 103px;
    width: 768px;
    height: 994px;
    display: block;
  }
  .paper { fill: var(--paper); }
  .band-dark { fill: var(--ink-dark); }
  .band-yellow { fill: var(--accent-yellow); }
  .stroke-yellow { fill: none; stroke: var(--accent-yellow); stroke-width: 4; }
  .brand-mark { fill: var(--brand-gold); }
  .brand-name {
    font-family: "Cinzel", serif;
    font-size: 60px;
    fill: var(--brand-gold);
  }
  .signer-name {
    font-family: "Noto Serif", serif;
    font-weight: 700;
    font-size: 26px;
    fill: var(--text-light);
    letter-spacing: 0.5px;
  }
  .signer-title {
    font-family: "Noto Serif", serif;
    font-style: italic;
    font-size: 25px;
    fill: var(--text-light);
  }
  .website {
    font-family: "Open Sans", sans-serif;
    font-size: 22px;
    fill: var(--text-light);
  }
</style>
</head>
<body>
<svg class="letterhead" viewBox="0 0 800 1036" xmlns="http://www.w3.org/2000/svg">
  <rect class="paper" x="0" y="0" width="800" height="1036"/>

  <!-- header swoosh -->
  <path class="band-dark" d="M0 0 H800 V112 C640 80 470 18 300 20 C180 22 80 60 0 100 Z"/>
  <path class="band-yellow" d="M0 100 C80 60 180 22 300 20 C470 18 640 80 800 112 V126 C640 92 470 30 300 32 C180 34 80 70 0 108 Z"/>
  <path class="stroke-yellow" d="M0 80 C80 38 180 10 280 0"/>

  <!-- brand -->
  <circle class="brand-mark" cx="92" cy="155" r="30"/>
  <text class="brand-name" x="160" y="178">BRAMWELL</text>

  <!-- footer swoosh -->
  <path class="band-yellow" d="M0 1036 C300 1010 600 920 800 755 V1036 Z"/>
  <path class="band-dark" d="M230 1036 C470 990 650 900 800 775 V1036 Z"/>

  <!-- signature block -->
  <text class="signer-name" x="776" y="944" text-anchor="end">Marisol Denby</text>
  <text class="signer-title" x="776" y="976" text-anchor="end">President</text>
  <text class="website" x="778" y="1016" text-anchor="end">www.bramwellllc-example.com</text>
</svg>
</body>
</html>
```